Three diagrams for an academic paper

I need professional-looking versions of three diagrams for an academic paper. I am uploading JPEGs of each diagram drafted in Vextra Docs. I need completely new versions that look much better.

Some detailed requirements:
- Professional styling - must be clearly superior to the ‘stick-figure’ example images and obviously not from powerpoint, etc.
- Must be a coordinated style across all three illustrations.
- Note that a mini-version of figure 2 appears in figure 3 (within the database image)
- I need very high resolution, suitable for a manuscript
- May need some text changes at short notice (anticipate 2 small updates to text)

Target Market(s)

Academics

Industry/Entity Type

Vextra

Font styles to use
Sans Serif

Colors

Designer to choose colors to be used in the design.

Requirements
Must have
• Don't look like powerpoint

```html
<!DOCTYPE html>
<html lang="en">
<head>
<meta charset="utf-8">
<title>Semiotic Triangle: Natural Language and Structured Data</title>
<link rel="stylesheet" href="https://fonts.googleapis.com/css2?family=Lato:wght@400;700;900&display=swap">
<style>
  :root {
    --navy: #0c1446;
    --navy-light: #2b3b8c;
    --salmon: #f47461;
    --red: #e3101b;
    --black: #000000;
    --white: #ffffff;
    --silver-dark: #c5c9cf;
    --silver-light: #eef1f4;
  }
  html, body {
    margin: 0;
    padding: 0;
    overflow: hidden;
    background: var(--white);
  }
  .canvas {
    position: relative;
    width: 1200px;
    height: 1200px;
    overflow: hidden;
    background: var(--white);
    font-family: "Lato", sans-serif;
  }
  .disk {
    position: absolute;
    border-radius: 50%;
  }
  .disk--structured {
    width: 1032px; height: 1032px;
    left: 84px; top: 88px;
    background: conic-gradient(
      #e8232a 0deg, var(--salmon) 25deg, var(--red) 50deg, var(--salmon) 90deg,
      #ec4a42 130deg, var(--salmon) 160deg, var(--red) 180deg, var(--salmon) 210deg,
      var(--salmon) 250deg, var(--red) 300deg, var(--salmon) 332deg, #e8232a 360deg);
  }
  .disk--relation {
    width: 872px; height: 872px;
    left: 164px; top: 168px;
    background: var(--black);
  }
  .disk--natural {
    width: 752px; height: 752px;
    left: 224px; top: 228px;
    background: conic-gradient(
      var(--navy) 0deg, var(--navy-light) 40deg, var(--navy) 100deg,
      var(--navy-light) 180deg, var(--navy) 250deg, var(--navy-light) 300deg,
      var(--navy) 360deg);
  }
  .disk--centre {
    width: 600px; height: 600px;
    left: 300px; top: 304px;
    background: var(--white);
  }
  .diagram {
    position: absolute;
    inset: 0;
  }
  .ring-label { fill: var(--white); }
  .ring-label--structured { font-size: 24px; font-weight: 700; }
  .ring-label--relation { font-size: 26px; font-weight: 900; letter-spacing: 1px; }
  .ring-label--natural { font-size: 21px; font-weight: 700; }
  .node-frame { fill: var(--black); }
  .node-face { fill: url(#silver); }
  .node-label {
    font-size: 35px;
    font-weight: 900;
    fill: #111111;
  }
  .legend-swatch--natural { fill: var(--navy); }
  .legend-swatch--structured { fill: var(--salmon); }
  .legend-text { font-size: 27px; font-weight: 900; }
  .legend-text--natural { fill: var(--navy); }
  .legend-text--structured { fill: var(--salmon); }
</style>
</head>
<body>
<div class="canvas">
  <div class="disk disk--structured"></div>
  <div class="disk disk--relation"></div>
  <div class="disk disk--natural"></div>
  <div class="disk disk--centre"></div>

  <svg class="diagram" viewBox="0 0 1200 1200" width="1200" height="1200" xmlns="http://www.w3.org/2000/svg">
    <defs>
      <linearGradient id="silver" x1="0" y1="0" x2="1" y2="1">
        <stop offset="0" stop-color="var(--silver-dark)"/>
        <stop offset="0.5" stop-color="var(--silver-light)"/>
        <stop offset="1" stop-color="var(--silver-dark)"/>
      </linearGradient>
      <path id="arc-structured-top" d="M132 604 A468 468 0 1 1 1068 604 A468 468 0 1 1 132 604"/>
      <path id="arc-relation-top" d="M204 604 A396 396 0 1 1 996 604 A396 396 0 1 1 204 604"/>
      <path id="arc-natural-top" d="M269 604 A331 331 0 1 1 931 604 A331 331 0 1 1 269 604"/>
      <path id="arc-structured-bottom" d="M116 604 A484 484 0 0 0 1084 604"/>
      <path id="arc-relation-bottom" d="M184 604 A416 416 0 0 0 1016 604"/>
      <path id="arc-natural-bottom" d="M255 604 A345 345 0 0 0 945 604"/>
    </defs>

    <g class="ring-labels" text-anchor="middle">
      <text class="ring-label ring-label--structured"><textPath href="#arc-structured-top" startOffset="10%">A thing or concept in the world</textPath></text>
      <text class="ring-label ring-label--relation"><textPath href="#arc-relation-top" startOffset="10%">SYMBOLIZES</textPath></text>
      <text class="ring-label ring-label--natural"><textPath href="#arc-natural-top" startOffset="10%">A thing or concept in the world</textPath></text>

      <text class="ring-label ring-label--structured"><textPath href="#arc-structured-top" startOffset="40.6%">A concept in the mind</textPath></text>
      <text class="ring-label ring-label--relation"><textPath href="#arc-relation-top" startOffset="40.6%">REFERS TO</textPath></text>
      <text class="ring-label ring-label--natural"><textPath href="#arc-natural-top" startOffset="40.6%">A unique identifier</textPath></text>

      <text class="ring-label ring-label--structured"><textPath href="#arc-structured-bottom" startOffset="50%">Words or phrases</textPath></text>
      <text class="ring-label ring-label--relation"><textPath href="#arc-relation-bottom" startOffset="50%">STANDS FOR</textPath></text>
      <text class="ring-label ring-label--natural"><textPath href="#arc-natural-bottom" startOffset="50%">A patterns of symbols</textPath></text>
    </g>

    <g class="node node--reference">
      <circle class="node-frame" cx="600" cy="204" r="136"/>
      <circle class="node-face" cx="600" cy="204" r="122"/>
      <text class="node-label" x="603" y="217" text-anchor="middle">REFERENCE</text>
    </g>
    <g class="node node--referent">
      <circle class="node-frame" cx="222" cy="772" r="136"/>
      <circle class="node-face" cx="222" cy="772" r="122"/>
      <text class="node-label" x="222" y="786" text-anchor="middle">REFERENT</text>
    </g>
    <g class="node node--symbol">
      <circle class="node-frame" cx="978" cy="772" r="136"/>
      <circle class="node-face" cx="978" cy="772" r="122"/>
      <text class="node-label" x="980" y="789" text-anchor="middle">SYMBOL</text>
    </g>

    <g class="legend">
      <rect class="legend-swatch--natural" x="466" y="521" width="72" height="72"/>
      <text class="legend-text legend-text--natural" x="557" y="551">NATURAL</text>
      <text class="legend-text legend-text--natural" x="557" y="580">LANGUAGE</text>
      <rect class="legend-swatch--structured" x="466" y="607" width="72" height="72"/>
      <text class="legend-text legend-text--structured" x="553" y="640">STRUCTURED</text>
      <text class="legend-text legend-text--structured" x="553" y="669">DATA</text>
    </g>
  </svg>
</div>
</body>
</html>
```